Open Red Harbor.. a non profit that seeks to stomp out skin cancer .. quiet paths toward opening red

Simple letterhead incorporating logo

Industry/Entity Type

Non Profit

Font styles to use
Sans Serif

Colors

Designer to choose colors to be used in the design.

```html
<!DOCTYPE html>
<html lang="en">
<head>
<meta charset="utf-8">
<title>Open Red Harbor — Letterhead</title>
<link rel="stylesheet" href="https://fonts.googleapis.com/css2?family=Raleway:wght@400&display=swap">
<style>
  :root {
    --navy: #232a3d;
    --yellow: #f5e100;
    --paper: #ffffff;
    --backdrop: #ebe6df;
  }
  html, body {
    margin: 0;
    padding: 0;
    width: 1200px;
    height: 1080px;
    overflow: hidden;
    background: var(--backdrop);
  }
  .canvas {
    position: relative;
    width: 1200px;
    height: 1080px;
  }
  .letterhead {
    position: absolute;
    left: 323px;
    top: 40px;
    width: 554px;
    height: 1000px;
    background: var(--paper);
    box-shadow: 0 6px 24px rgba(35, 42, 61, 0.18);
  }
  .letterhead__art {
    position: absolute;
    inset: 0;
    width: 554px;
    height: 1000px;
    display: block;
  }
  .brand {
    position: absolute;
    left: 62px;
    top: 92px;
    display: flex;
    align-items: center;
    gap: 14px;
  }
  .brand__dot {
    width: 62px;
    height: 62px;
    border-radius: 50%;
    background: var(--navy);
    flex: none;
  }
  .brand__name {
    margin: 0;
    font-family: "Raleway", sans-serif;
    font-weight: 400;
    font-size: 27px;
    letter-spacing: 0.5px;
    color: var(--navy);
    white-space: nowrap;
  }
</style>
</head>
<body>
<main class="canvas">
  <section class="letterhead" aria-label="Open Red Harbor letterhead">
    <svg class="letterhead__art" viewBox="0 0 475 857" aria-hidden="true">
      <!-- top corner and band -->
      <polygon class="corner-top" points="0,0 118,0 0,205" fill="var(--yellow)"/>
      <polygon class="band-top" points="118,0 475,0 475,34 98,34" fill="var(--navy)"/>

      <!-- contact icon column -->
      <rect class="contact-strip" x="418" y="57" width="34" height="173" fill="var(--yellow)"/>
      <!-- phone -->
      <path class="icon-phone" d="M431 68 q-5 4 -2 14 q3 9 10 13 q3 1 5 -1 l1 -3 l-4 -3 l-2 2 q-4 -3 -5 -8 l2 -1 l-1 -5 z" fill="var(--navy)"/>
      <!-- fax -->
      <g class="icon-fax" fill="none" stroke="var(--navy)" stroke-width="1.6">
        <rect x="428" y="131" width="12" height="7"/>
        <rect x="425" y="138" width="18" height="9"/>
        <line x1="428" y1="144" x2="440" y2="144"/>
      </g>
      <!-- mail -->
      <g class="icon-mail" fill="none" stroke="var(--navy)" stroke-width="1.6">
        <rect x="422" y="197" width="26" height="18"/>
        <polyline points="422,197 435,208 448,197"/>
        <line x1="422" y1="215" x2="431" y2="206"/>
        <line x1="448" y1="215" x2="439" y2="206"/>
      </g>

      <!-- web icon -->
      <rect class="web-square" x="16" y="785" width="36" height="37" fill="var(--yellow)"/>
      <g class="icon-web" fill="none" stroke="var(--navy)" stroke-width="1.5">
        <circle cx="34" cy="803.5" r="11" fill="var(--navy)"/>
        <ellipse cx="34" cy="803.5" rx="5" ry="11" stroke="var(--yellow)" stroke-width="1"/>
        <line x1="23" y1="803.5" x2="45" y2="803.5" stroke="var(--yellow)" stroke-width="1"/>
      </g>

      <!-- bottom band and corner -->
      <polygon class="band-bottom" points="0,822 355,822 333,857 0,857" fill="var(--navy)"/>
      <polygon class="corner-bottom" points="475,635 475,857 333,857" fill="var(--yellow)"/>
    </svg>

    <div class="brand">
      <span class="brand__dot"></span>
      <h1 class="brand__name">Open Red Harbor</h1>
    </div>
  </section>
</main>
</body>
</html>
```